Cosmetics Brand Logo and Bottle Label Design

We are creating a new cosmetics brand called "Nolan Whitby" and would like you to create an amazing logo and bottle label for this brand's new 100% pure argan oil product.
For the logo, we really like the logo's of Marin Calloway and Vessa. The text should be Sans Serif (without feet).
For the actual bottle label, please find attached labels of one of our competitors design which really like. We really like the simplicity and elegance of the design. The only difference is that our product will be using light turqoise as the brand color. Please feel free to add your own creativity into it as well.
Industry/Entity Type
Cosmetics
Logo Text
Nolan Whitby
Font styles to use

```html
<!DOCTYPE html>
<html lang="en">
<head>
<meta charset="UTF-8">
<title>Nolan Whitby – Argan Oil Label</title>
<link rel="stylesheet" href="https://fonts.googleapis.com/css2?family=Roboto:wght@300;400;500&display=swap">
<style>
  :root {
    --label-bg: #8bd2c5;
    --pattern-tone: #9ad8cc;
    --badge-teal: #2fb7a1;
    --ink-white: #ffffff;
    --ink-dark: #3b3b3b;
  }
  html, body {
    margin: 0;
    padding: 0;
    width: 1200px;
    height: 626px;
    overflow: hidden;
    background: var(--label-bg);
  }
  .label {
    position: relative;
    width: 1200px;
    height: 626px;
    background: var(--label-bg);
    font-family: "Roboto", Arial, sans-serif;
    overflow: hidden;
  }
  .pattern-panel {
    position: absolute;
    top: 0;
    height: 626px;
    background: linear-gradient(180deg, var(--pattern-tone), var(--label-bg) 50%, var(--pattern-tone));
  }
  .pattern-panel--left { left: 0; width: 410px; }
  .pattern-panel--right { left: 805px; width: 395px; }
  .brand-badge {
    position: absolute;
    left: 0;
    top: 0;
    width: 1200px;
    height: 626px;
  }
  .brand-name {
    position: absolute;
    left: 420px;
    top: 190px;
    width: 330px;
    text-align: center;
    color: var(--ink-white);
    font-weight: 300;
    font-size: 66px;
    line-height: 70px;
    letter-spacing: 1px;
    margin: 0;
  }
  .brand-tagline {
    position: absolute;
    left: 410px;
    top: 354px;
    width: 340px;
    text-align: center;
    color: var(--ink-white);
    font-weight: 400;
    font-size: 26px;
    margin: 0;
  }
  .product-info {
    position: absolute;
    left: 380px;
    top: 455px;
    width: 440px;
    text-align: center;
    color: var(--ink-dark);
  }
  .product-info p { margin: 0; }
  .product-type { font-weight: 300; font-size: 46px; line-height: 54px; }
  .product-desc { font-weight: 400; font-size: 29px; line-height: 42px; }
  .product-volume { font-weight: 500; font-size: 29px; line-height: 44px; }
</style>
</head>
<body>
<main class="label">
  <div class="pattern-panel pattern-panel--left" role="img" aria-label="Decorative repeating swirl-and-dot pattern in pale turquoise"></div>
  <div class="pattern-panel pattern-panel--right" role="img" aria-label="Decorative repeating swirl-and-dot pattern in pale turquoise"></div>

  <svg class="brand-badge" viewBox="0 0 1200 626" aria-hidden="true">
    <circle cx="604" cy="182" r="168" fill="var(--badge-teal)"/>
    <circle cx="466" cy="278" r="72" fill="var(--badge-teal)"/>
    <circle cx="600" cy="300" r="110" fill="var(--badge-teal)"/>
  </svg>

  <h1 class="brand-name">nolan<br>whitby</h1>
  <p class="brand-tagline">100% pure argan oil</p>

  <section class="product-info">
    <p class="product-type">organic</p>
    <p class="product-desc">moisturizing oil</p>
    <p class="product-volume">50mL 1.7 fl oz</p>
  </section>
</main>
</body>
</html>
```